Kestrow Fire Services Pty Ltd

We need business cards for a company based in Perth, we install, service and maintain fire equipment.
On the front we want a great design with our logo and a small spot for our full company name, general company email address and office number. On the back we need space for our name, title, mobile number and email address on the back.

Target Market(s)

Facility managers and commercial/industrial building owners/occupiers.

Contact Information for Business Card

Font styles to use
Sans Serif

Requirements
Must have
• Please only submit 5 of your best samples.
Darker tones are preferred.
Nice to have
• We want to use, black, red and grey. Keep it modern and clean.
I've attached the company logo and a sample of a boarder we use on our emergency plans.
Should not have
• No preference. Let the designer choose.

```html
<!DOCTYPE html>
<html lang="en">
<head>
<meta charset="utf-8">
<title>Kestrow Fire Services – Business Cards</title>
<link rel="stylesheet" href="https://fonts.googleapis.com/css2?family=Oswald:wght@500;600&family=Montserrat:wght@400;500&display=swap">
<style>
  :root {
    --bg: #161616;
    --card: #0b0b0b;
    --red: #d8232a;
    --red-deep: #b51c22;
    --white: #f2f2f2;
    --grey: #bdbdbd;
    --ink: #111111;
  }
  * { box-sizing: border-box; margin: 0; padding: 0; }
  html, body {
    width: 1200px; height: 900px; overflow: hidden;
    background: radial-gradient(ellipse at 50% 40%, #222 0%, var(--bg) 70%);
    font-family: "Montserrat", sans-serif;
  }
  .stage {
    position: relative; width: 1200px; height: 900px;
    display: flex; align-items: center; justify-content: center; gap: 60px;
  }
  .card {
    position: relative; width: 500px; height: 290px;
    background: var(--card); border-radius: 26px; overflow: hidden;
    box-shadow: 0 20px 40px rgba(0,0,0,.55);
  }
  .brand-name {
    font-family: "Oswald", sans-serif; font-weight: 600;
    color: var(--red); text-transform: uppercase; letter-spacing: 1px; line-height: 1;
  }
  .contact-list { list-style: none; display: flex; flex-direction: column; gap: 9px; }
  .contact-item {
    display: flex; align-items: center; gap: 10px;
    color: var(--white); font-size: 14px; letter-spacing: .3px; white-space: nowrap;
  }
  .contact-item svg { width: 13px; height: 13px; fill: var(--red); flex: none; }

  /* Front */
  .card--front .brand-name { position: absolute; left: 40px; top: 48px; font-size: 66px; }
  .company-band {
    position: absolute; left: 40px; right: 0; top: 140px; height: 18px;
    background: var(--red-deep);
    font-family: "Oswald", sans-serif; font-weight: 500; font-size: 13px;
    color: var(--ink); text-transform: uppercase; letter-spacing: 1.2px;
    line-height: 18px; padding-left: 6px;
  }
  .card--front .contact-list { position: absolute; right: 40px; top: 182px; }

  /* Back */
  .holder { position: absolute; left: 32px; top: 30px; }
  .holder-name {
    font-family: "Oswald", sans-serif; font-weight: 600; font-size: 22px;
    color: var(--white); text-transform: uppercase; letter-spacing: .5px;
  }
  .holder-title {
    font-family: "Oswald", sans-serif; font-weight: 500; font-size: 12px;
    color: var(--red); text-transform: uppercase; letter-spacing: 1px;
  }
  .holder-rule { width: 34px; height: 2px; background: var(--red); margin-top: 12px; }
  .card--back .contact-list { position: absolute; left: 32px; bottom: 40px; }
  .card--back .contact-item { font-size: 13px; color: var(--grey); }
  .card--back .brand-name { position: absolute; right: 30px; bottom: 60px; font-size: 46px; }
</style>
</head>
<body>
<main class="stage">
  <section class="card card--front" aria-label="Card front">
    <div class="brand-name">Kestrow</div>
    <div class="company-band">Kestrow Fire Services Pty Ltd</div>
    <ul class="contact-list">
      <li class="contact-item">
        <svg viewBox="0 0 24 24" aria-hidden="true"><path d="M6.6 10.8a15.1 15.1 0 0 0 6.6 6.6l2.2-2.2c.3-.3.7-.4 1-.2 1.1.4 2.3.6 3.6.6.6 0 1 .4 1 1V20c0 .6-.4 1-1 1A17 17 0 0 1 3 4c0-.6.4-1 1-1h3.5c.6 0 1 .4 1 1 0 1.3.2 2.5.6 3.6.1.3 0 .7-.2 1z"/></svg>
        1300 482 615
      </li>
      <li class="contact-item">
        <svg viewBox="0 0 24 24" aria-hidden="true"><path d="M2 5h20v14H2zm2 2v.5l8 5 8-5V7z"/></svg>
        info@kestrowfire.com.au
      </li>
    </ul>
  </section>

  <section class="card card--back" aria-label="Card back">
    <div class="holder">
      <div class="holder-name">Marco Delvane</div>
      <div class="holder-title">Director</div>
      <div class="holder-rule"></div>
    </div>
    <ul class="contact-list">
      <li class="contact-item">
        <svg viewBox="0 0 24 24" aria-hidden="true"><path d="M6.6 10.8a15.1 15.1 0 0 0 6.6 6.6l2.2-2.2c.3-.3.7-.4 1-.2 1.1.4 2.3.6 3.6.6.6 0 1 .4 1 1V20c0 .6-.4 1-1 1A17 17 0 0 1 3 4c0-.6.4-1 1-1h3.5c.6 0 1 .4 1 1 0 1.3.2 2.5.6 3.6.1.3 0 .7-.2 1z"/></svg>
        0412 557 318
      </li>
      <li class="contact-item">
        <svg viewBox="0 0 24 24" aria-hidden="true"><path d="M2 5h20v14H2zm2 2v.5l8 5 8-5V7z"/></svg>
        marco@kestrowfire.com.au
      </li>
    </ul>
    <div class="brand-name">Kestrow</div>
  </section>
</main>
</body>
</html>
```